Presentation for new businessconcept from mediacompany

We have a need of an presentation for our bussinessidea within media.

Attatched is the presentation in text, we need illustrations that shows what we can do in same graphic theme as our logo and site: www.mirolanta-web.com

As little text as possible since we will use this for presentations but u should still be able to understand every slide without hearing the words.

Please PM me for more info, possible movieproject for same issue will be relevant in beginning of next year as well.

The Quillomo-bee is right now attatched on the logo so feel free to play with him, just as long we can tell he is the one there :)

Forget to say, the presentation is going to be in swedish so we will change all the text, please use images only according to the description.

People who work with marketing and communication i all kinds of companies.

Media

• The files we upload is the logo and a rough example of situations we like our quillomo-bee to be in in the presentation. you are free to come with other suggestions, this is only to give you a hint of what we are looking for.
Please use same colors as we have on www.mirolanta-web.com
• We would really love it if our Mirolanta Bee were to be an important part in all the slides, like showing, pointing, acting etc in different forms.
• We dont want photos or real people, we like it more like a cartoon with our Mirolanta bee as a maincharrachter.

```html
<!DOCTYPE html>
<html lang="en">
<head>
<meta charset="utf-8">
<title>Implementation</title>
<link rel="stylesheet" href="https://fonts.googleapis.com/css2?family=Sniglet:wght@400&family=Arimo:wght@700&display=swap">
<style>
  :root {
    --paper: #ececea;
    --paper-shade: #e2e2df;
    --white: #ffffff;
    --title-green: #a6c11c;
    --rule-olive: #6a6b1d;
    --label-ink: #3a3a3a;
    --arrow-grey: #8f8f8f;
    --puzzle-light: #b9b9b9;
    --puzzle-dark: #4c4c4c;
    --brand-olive: #6f7120;
    --magnet-red: #c8332c;
    --steel: #b8bcc2;
    --switch-green: #3bb34a;
    --switch-red: #d8312b;
    --gift-red: #e0322a;
    --gift-ribbon: #f4c21c;
    --screen-frame: #5b5f66;
    --chart-line: #d3241c;
  }
  * { margin: 0; padding: 0; box-sizing: border-box; }
  html, body { width: 1200px; height: 656px; overflow: hidden; }
  body {
    position: relative;
    background: radial-gradient(ellipse at 40% 45%, var(--paper) 0%, var(--paper-shade) 100%);
    font-family: "Arimo", Arial, sans-serif;
  }
  .slide { position: absolute; inset: 0; }
  .backdrop { position: absolute; inset: 0; }
  .title-mark {
    position: absolute; left: 240px; top: 82px;
    width: 16px; height: 16px; border-radius: 50%;
    background: var(--rule-olive);
  }
  .slide-title {
    position: absolute; left: 297px; top: 58px;
    font-family: "Sniglet", "Comic Sans MS", cursive;
    font-weight: 400; font-size: 33px; letter-spacing: 0.3px;
    color: var(--title-green);
  }
  .step {
    position: absolute; top: 256px; width: 160px;
    text-align: center;
  }
  .step-label {
    font-size: 15px; font-weight: 700; color: var(--label-ink);
    letter-spacing: -0.2px; height: 20px;
  }
  .step-disc {
    margin: 12px auto 0; width: 124px; height: 124px; border-radius: 50%;
    background: var(--white); position: relative; overflow: hidden;
  }
  .step-icon { position: absolute; inset: 0; }
  .puzzle-piece, .puzzle-globe { position: absolute; }
  .puzzle-piece {
    left: 988px; top: 368px; width: 92px; height: 80px;
    border-radius: 10px; transform: rotate(-16deg);
    background: linear-gradient(150deg, var(--puzzle-light), #6e6e6e);
  }
  .puzzle-globe {
    left: 1010px; top: 476px; width: 260px; height: 240px; border-radius: 50%;
    background: radial-gradient(circle at 35% 25%, #d4d4d4, var(--puzzle-dark) 70%);
  }
  .brand {
    position: absolute; left: 962px; top: 600px;
    display: flex; align-items: center; gap: 6px;
  }
  .brand-dot { width: 10px; height: 10px; border-radius: 50%; background: var(--brand-olive); }
  .brand-name {
    font-family: "Sniglet", "Comic Sans MS", cursive; font-weight: 400;
    font-size: 19px; color: var(--brand-olive);
  }
</style>
</head>
<body>
<main class="slide">
  <svg class="backdrop" width="1200" height="656" viewBox="0 0 1200 656" aria-hidden="true">
    <path d="M1200 12 C1040 120 880 250 885 380 C890 470 990 560 1200 592 Z" fill="var(--white)"/>
    <path d="M232 106 L1022 106 Q1042 106 1044 124" fill="none" stroke="var(--rule-olive)" stroke-width="3" stroke-linecap="round"/>
    <g fill="none" stroke="var(--arrow-grey)" stroke-width="2.5" stroke-linecap="round">
      <path d="M360 306 Q378 288 400 298"/>
      <path d="M392 292 L401 298 L392 304"/>
      <path d="M520 390 Q536 408 562 396"/>
      <path d="M553 392 L563 396 L556 404"/>
      <path d="M676 304 Q694 286 718 296"/>
      <path d="M709 290 L719 296 L710 303"/>
    </g>
  </svg>

  <span class="title-mark"></span>
  <h1 class="slide-title">Implementation</h1>

  <section class="process">
    <div class="step" style="left:230px">
      <p class="step-label">The attraction</p>
      <div class="step-disc">
        <svg class="step-icon" viewBox="0 0 124 124" role="img" aria-label="Magnet pulling people in">
          <path d="M78 40 H60 a22 22 0 0 0 0 44 H78" fill="none" stroke="var(--magnet-red)" stroke-width="14"/>
          <rect x="74" y="33" width="14" height="14" fill="var(--steel)"/>
          <rect x="74" y="77" width="14" height="14" fill="var(--steel)"/>
          <g stroke="var(--arrow-grey)" stroke-width="2.5" stroke-linecap="round">
            <path d="M94 40 H104"/><path d="M94 84 H104"/><path d="M96 62 H106"/>
          </g>
        </svg>
      </div>
    </div>
    <div class="step" style="left:388px">
      <p class="step-label">Activation</p>
      <div class="step-disc">
        <svg class="step-icon" viewBox="0 0 124 124" role="img" aria-label="On and off toggle switch">
          <path d="M34 62 V38 a16 16 0 0 1 16 -16 H74 a16 16 0 0 1 16 16 V62 Z" fill="var(--switch-green)"/>
          <path d="M34 62 V86 a16 16 0 0 0 16 16 H74 a16 16 0 0 0 16 -16 V62 Z" fill="var(--switch-red)"/>
          <text x="62" y="44" text-anchor="middle" font-family="Arimo, Arial, sans-serif" font-weight="700" font-size="13" fill="var(--white)">ON</text>
          <text x="62" y="92" text-anchor="middle" font-family="Arimo, Arial, sans-serif" font-weight="700" font-size="13" fill="var(--white)">OFF</text>
          <rect x="52" y="54" width="20" height="16" rx="3" fill="var(--steel)"/>
          <path d="M62 62 L92 48" stroke="var(--steel)" stroke-width="6" stroke-linecap="round"/>
          <circle cx="94" cy="47" r="7" fill="#d9dde2"/>
        </svg>
      </div>
    </div>
    <div class="step" style="left:547px">
      <p class="step-label">Reward</p>
      <div class="step-disc">
        <svg class="step-icon" viewBox="0 0 124 124" role="img" aria-label="Gift box handed over as a reward">
          <rect x="36" y="54" width="52" height="44" fill="var(--gift-red)"/>
          <rect x="32" y="44" width="60" height="14" fill="var(--gift-red)"/>
          <rect x="56" y="44" width="12" height="54" fill="var(--gift-ribbon)"/>
          <path d="M62 44 C50 26 34 32 44 44 Z M62 44 C74 26 90 32 80 44 Z" fill="none" stroke="var(--gift-red)" stroke-width="5"/>
        </svg>
      </div>
    </div>
    <div class="step" style="left:707px">
      <p class="step-label">Feedback</p>
      <div class="step-disc">
        <svg class="step-icon" viewBox="0 0 124 124" role="img" aria-label="Laptop showing a rising results chart">
          <rect x="32" y="34" width="60" height="42" rx="3" fill="var(--screen-frame)"/>
          <rect x="36" y="38" width="52" height="34" fill="var(--white)"/>
          <path d="M40 66 L52 58 L60 62 L72 48 L84 42" fill="none" stroke="var(--chart-line)" stroke-width="2.5" stroke-linejoin="round"/>
          <path d="M78 41 L85 41 L83 48" fill="none" stroke="var(--chart-line)" stroke-width="2.5"/>
          <path d="M26 80 H98 L94 88 H30 Z" fill="#8b9098"/>
        </svg>
      </div>
    </div>
  </section>

  <div class="puzzle-piece" role="img" aria-label="Loose grey puzzle piece"></div>
  <div class="puzzle-globe" role="img" aria-label="Sphere built from grey puzzle pieces"></div>

  <div class="brand">
    <span class="brand-dot"></span>
    <span class="brand-name">Mirolanta</span>
  </div>
</main>
</body>
</html>
```